Business cards for Brightmarrow Consulting with the following info for the front side:

Brightmarrow Consulting
Executive Coaching and Human Capital Strategy
www.brightmarrow.example

Lorena Vaduvic
Principal
lorena@brightmarrow.example
+1 604 555 0172

Black background, text using the colours of the logo - enclosed.

The back side of the business card should feature the logo in the middle, with "Executive Coaching and Human Capital Strategy" on top and "www.brightmarrow.example" below.

```html
<!DOCTYPE html>
<html lang="en">
<head>
<meta charset="utf-8">
<title>Brightmarrow Consulting – Business Cards</title>
<link rel="stylesheet" href="https://fonts.googleapis.com/css2?family=Poppins:wght@400;500;600;700&display=swap">
<style>
  :root {
    --stage: #3a3f46;
    --card-black: #0b0b0b;
    --brand-blue: #31a3d8;
    --brand-yellow: #fbbf1a;
    --text-white: #ffffff;
  }
  * { margin: 0; padding: 0; box-sizing: border-box; }
  html, body {
    width: 1200px; height: 900px; overflow: hidden;
    background: var(--stage);
    font-family: "Poppins", sans-serif;
  }
  .stage {
    width: 1200px; height: 900px;
    display: flex; flex-direction: column;
    align-items: center; justify-content: center; gap: 40px;
  }
  .card {
    position: relative;
    width: 700px; height: 400px;
    background: var(--card-black);
    border-radius: 4px;
    overflow: hidden;
    box-shadow: 0 10px 30px rgba(0,0,0,0.45);
  }

  /* Logo-side card */
  .brand-lockup {
    position: absolute; inset: 0;
    display: flex; align-items: center; justify-content: center;
  }
  .brand-mark {
    width: 92px; height: 92px; border-radius: 50%;
    border: 5px solid var(--brand-blue);
    margin-right: 18px; flex-shrink: 0;
  }
  .brand-text { display: flex; flex-direction: column; }
  .brand-name {
    color: var(--brand-blue);
    font-weight: 700; font-size: 50px; line-height: 1;
    letter-spacing: 1px;
  }
  .brand-tagline {
    color: var(--text-white);
    font-weight: 600; font-size: 15.5px;
    margin-top: 8px;
  }
  .brand-url {
    color: var(--brand-blue);
    font-weight: 500; font-size: 15px;
    letter-spacing: 7.4px; margin-top: 4px;
  }

  /* Person card */
  .card-waves { position: absolute; inset: 0; }
  .person-mark {
    position: absolute; left: 60px; top: 40px;
    display: flex; align-items: center; gap: 14px;
  }
  .person-mark .dot {
    width: 70px; height: 70px; border-radius: 50%;
    border: 5px solid var(--brand-blue);
  }
  .person-mark .word {
    color: var(--brand-yellow); font-weight: 600; font-size: 22px;
  }
  .person {
    position: absolute; right: 50px; top: 150px; text-align: right;
  }
  .person-name {
    color: var(--brand-yellow); font-weight: 600; font-size: 30px; line-height: 1.1;
  }
  .person-role {
    color: var(--brand-blue); font-weight: 400; font-size: 17px;
  }
  .contact {
    position: absolute; left: 40px; top: 236px; width: 320px;
    list-style: none; text-align: right;
  }
  .contact li {
    color: var(--text-white); font-size: 16px; line-height: 28px;
    display: flex; justify-content: flex-end; align-items: center; gap: 10px;
  }
  .contact svg { width: 16px; height: 16px; flex-shrink: 0; }
</style>
</head>
<body>
<main class="stage">

  <section class="card card-logo-side" aria-label="Card back">
    <div class="brand-lockup">
      <div class="brand-mark"></div>
      <div class="brand-text">
        <span class="brand-name">BRIGHTMARROW</span>
        <span class="brand-tagline">Executive Coaching and Human Capital Strategy</span>
        <span class="brand-url">www.brightmarrow.example</span>
      </div>
    </div>
  </section>

  <section class="card card-person-side" aria-label="Card front">
    <svg class="card-waves" viewBox="0 0 700 400" preserveAspectRatio="none">
      <path d="M0,150 C170,165 330,230 450,400 L0,400 Z" fill="var(--brand-blue)"/>
      <path d="M70,190 C190,210 320,260 420,340 C320,250 200,215 70,190 Z" fill="var(--card-black)"/>
      <path d="M0,110 C110,105 250,150 330,230 C240,165 120,130 0,125 Z" fill="var(--brand-yellow)"/>
    </svg>

    <div class="person-mark">
      <div class="dot"></div>
      <span class="word">Brightmarrow</span>
    </div>

    <div class="person">
      <div class="person-name">Lorena Vaduvic</div>
      <div class="person-role">Principal</div>
    </div>

    <ul class="contact">
      <li>+1 604 555 0172
        <svg viewBox="0 0 24 24" fill="var(--text-white)"><path d="M6.6 10.8a15 15 0 0 0 6.6 6.6l2.2-2.2a1 1 0 0 1 1-.25 11.4 11.4 0 0 0 3.6.57 1 1 0 0 1 1 1V20a1 1 0 0 1-1 1A17 17 0 0 1 3 4a1 1 0 0 1 1-1h3.5a1 1 0 0 1 1 1c0 1.25.2 2.45.57 3.6a1 1 0 0 1-.25 1z"/></svg>
      </li>
      <li>lorena@brightmarrow.example
        <svg viewBox="0 0 24 24" fill="none" stroke="var(--text-white)" stroke-width="2"><rect x="3" y="5" width="18" height="14" rx="1"/><path d="M3 6l9 7 9-7"/></svg>
      </li>
      <li>www.brightmarrow.example
        <svg viewBox="0 0 24 24" fill="none" stroke="var(--text-white)" stroke-width="2"><circle cx="12" cy="12" r="9"/><path d="M3 12h18M12 3c3 3 3 15 0 18M12 3c-3 3-3 15 0 18"/></svg>
      </li>
    </ul>
  </section>

</main>
</body>
</html>
```